Wirenexa

I'm looking to much improve our current website wirenexa.com
Updates

Low design quality

Target Market(s)

Commercial clients (Not-Residentials)

Industry/Entity Type

Office buildings and Industrial clients

Coding

Coded - Design and coding required

Number of Pages Required

5+ page

Requirements
Must have
• Very professional structured low voltage cabling projects for Wi-Fi, Audio/Video conference rooms, Access Control systems, CCTV.

```html
<!DOCTYPE html>
<html lang="en">
<head>
<meta charset="UTF-8">
<title>Wirenexa — Low Voltage Cabling</title>
<link href="https://fonts.googleapis.com/css2?family=Inter:wght@400;500;600;700;800;900&family=IBM+Plex+Mono:wght@400&display=swap" rel="stylesheet">
<style>
  :root{
    --bg:#0f0f0f;
    --bg-alt:#141414;
    --band:#1a1a1a;
    --line:#2a2a2a;
    --red:#d32a20;
    --white:#ffffff;
    --muted:#9a9a9a;
    --dim:#5c5c5c;
  }
  *{box-sizing:border-box;margin:0;padding:0}
  html,body{width:1200px;height:2504px;overflow:hidden}
  body{background:var(--bg);color:var(--white);font-family:"Inter",sans-serif}
  .wrap{width:1026px;margin:0 auto}

  .site-header{height:68px;border-bottom:1px solid var(--line);background:#0d0d0d}
  .site-header .wrap{display:flex;align-items:center;height:100%}
  .brand{display:flex;align-items:center;gap:10px;font-weight:700;font-size:26px;letter-spacing:-0.5px}
  .brand-mark{width:30px;height:30px;background:var(--red)}
  .nav{margin-left:auto;display:flex;align-items:center;gap:27px;font-size:12px;font-weight:500;letter-spacing:0.6px}
  .nav .cta{background:var(--red);padding:13px 20px}
  .theme-toggle{margin-left:14px;width:18px;height:18px}

  .hero{height:825px;position:relative;background:linear-gradient(100deg,#120c0b 0%,#231716 45%,#2d1f1d 75%,#1b1413 100%)}
  .hero-text{position:absolute;left:87px;top:220px;width:560px}
  .hero h1{font-weight:900;font-size:62px;line-height:1.08;letter-spacing:-1.5px;text-transform:uppercase}
  .hero h1 span{color:var(--red)}
  .hero p{margin-top:28px;font-size:17px;line-height:1.6;color:#e2e2e2}
  .hero-actions{margin-top:30px;display:flex;gap:13px}
  .btn{display:inline-flex;align-items:center;justify-content:center;height:40px;padding:0 20px;font-size:12px;font-weight:700;letter-spacing:0.8px;text-transform:uppercase}
  .btn-red{background:var(--red)}
  .btn-outline{border:1.5px solid var(--white)}

  .clients{height:88px;background:var(--band);border-bottom:1px solid var(--line);overflow:hidden;position:relative}
  .clients-row{position:absolute;left:-26px;top:0;height:100%;display:flex;align-items:center;gap:84px;white-space:nowrap;font-weight:800;font-size:18px;color:#555;text-transform:uppercase}

  .why{height:666px;position:relative}
  .why-text{position:absolute;left:87px;top:155px;width:420px}
  .why h2{font-size:40px;font-weight:700;line-height:1.2;letter-spacing:-0.5px}
  .why h2 span{color:var(--red)}
  .why p{margin-top:28px;font-size:13px;line-height:1.6;color:var(--muted)}
  .checklist{list-style:none;margin-top:30px}
  .checklist li{display:flex;align-items:center;gap:14px;font-size:13px;font-weight:500;height:35px}
  .checklist svg{width:18px;height:18px}
  .why-image{position:absolute;left:614px;top:81px;width:499px;height:503px;background:radial-gradient(circle at 50% 40%,#d8d8d8 0%,#6a6a6a 35%,#222 80%);border:1px solid var(--line)}

  .services{height:479px;background:var(--bg-alt);border-top:1px solid var(--line);border-bottom:1px solid var(--line)}
  .services-head{display:flex;justify-content:space-between;align-items:center;padding-top:85px}
  .services h2{font-size:40px;font-weight:700;letter-spacing:-0.5px}
  .services h2 span{color:var(--red)}
  .btn-small{height:41px;border:1.5px solid var(--white);padding:0 20px;font-size:12px;font-weight:700;letter-spacing:0.8px;display:flex;align-items:center;gap:8px}
  .cards{margin-top:40px;display:flex;gap:27px}
  .card{width:324px;height:228px;border:1px solid var(--line);padding:28px 27px}
  .card svg{width:26px;height:26px}
  .card h3{margin-top:22px;font-size:20px;font-weight:700}
  .card p{margin-top:18px;font-size:11.5px;line-height:1.6;color:var(--muted)}

  .site-footer{height:378px;background:var(--bg)}
  .footer-top{display:flex;padding-top:54px;height:305px;border-bottom:1px solid var(--line)}
  .footer-brand{width:527px}
  .footer-brand .brand{font-size:40px;gap:14px}
  .footer-brand .brand-mark{width:50px;height:50px}
  .footer-brand p{margin-top:30px;width:260px;font-size:13px;line-height:1.65;color:var(--muted)}
  .footer-col{width:263px}
  .footer-col h4{font-size:11px;font-weight:700;letter-spacing:0.4px;margin-top:6px}
  .footer-col ul{list-style:none;margin-top:14px}
  .footer-col li{font-size:11.5px;height:26px}
  .mono{font-family:"IBM Plex Mono",monospace;color:#aaa}
  .footer-bottom{display:flex;justify-content:space-between;align-items:center;height:72px;font-size:10px;color:#888}
  .footer-bottom nav{display:flex;gap:14px}
</style>
</head>
<body>
<header class="site-header">
  <div class="wrap">
    <div class="brand"><span class="brand-mark"></span>Wirenexa</div>
    <nav class="nav">
      <span>HOME</span><span>ABOUT US</span><span>SERVICES</span>
      <span class="cta">CONTACT US</span>
      <svg class="theme-toggle" viewBox="0 0 24 24" fill="none" stroke="#fff" stroke-width="2"><path d="M20 14.5A8 8 0 1 1 9.5 4a6.5 6.5 0 0 0 10.5 10.5z"/></svg>
    </nav>
  </div>
</header>

<section class="hero" role="img" aria-label="Dim server room aisle with racks and overhead cable trays">
  <div class="hero-text">
    <h1>Elevate your connectivity with <span>Wirenexa.</span></h1>
    <p>Your premier provider of professional low voltage cabling services in Virginia, Washington DC, and Maryland. We deliver exceptional cabling solutions for audio, video, security systems, and computer networks.</p>
    <div class="hero-actions">
      <span class="btn btn-red">Get a quote</span>
      <span class="btn btn-outline">View services</span>
    </div>
  </div>
</section>

<section class="clients">
  <div class="clients-row">
    <span>Health</span><span>Marquee Screens</span><span>Deskline</span><span>Agrifed</span><span>Northway Health</span><span>Marquee Screens</span>
  </div>
</section>

<section class="why">
  <div class="why-text">
    <h2>Why Choose<br><span>Wirenexa</span></h2>
    <p>We take pride in our work and strive for excellence in every project we undertake. Our cabling work is engineered and implemented with care and attention to detail, ensuring reliability, durability, and long-term performance.</p>
    <ul class="checklist">
      <li><svg viewBox="0 0 24 24" fill="none" stroke="#d32a20" stroke-width="2"><path d="M20 12v8H4V4h11"/><path d="M8 11l4 4 9-10"/></svg>Expertise and Experience</li>
      <li><svg viewBox="0 0 24 24" fill="none" stroke="#d32a20" stroke-width="2"><path d="M20 12v8H4V4h11"/><path d="M8 11l4 4 9-10"/></svg>Comprehensive Solutions</li>
      <li><svg viewBox="0 0 24 24" fill="none" stroke="#d32a20" stroke-width="2"><path d="M20 12v8H4V4h11"/><path d="M8 11l4 4 9-10"/></svg>Commercial and Industrial Focus</li>
      <li><svg viewBox="0 0 24 24" fill="none" stroke="#d32a20" stroke-width="2"><path d="M20 12v8H4V4h11"/><path d="M8 11l4 4 9-10"/></svg>Commitment to Customer Satisfaction</li>
    </ul>
  </div>
  <div class="why-image" role="img" aria-label="Black and white photo of server racks with neatly bundled network cables"></div>
</section>

<section class="services">
  <div class="wrap">
    <div class="services-head">
      <h2>Core <span>Services</span></h2>
      <span class="btn-small">VIEW ALL SERVICES <svg width="12" height="12" viewBox="0 0 24 24" fill="none" stroke="#fff" stroke-width="2.5"><path d="M4 12h16M14 6l6 6-6 6"/></svg></span>
    </div>
    <div class="cards">
      <article class="card">
        <svg viewBox="0 0 24 24" fill="none" stroke="#d32a20" stroke-width="2"><path d="M6 3v4M10 3v4M4 7h8v4a4 4 0 0 1-8 0z"/><path d="M8 15v3a3 3 0 0 0 6 0V8a3 3 0 0 1 6 0v5"/><path d="M18 13h4v4h-4z"/></svg>
        <h3>Structured Cabling</h3>
        <p>End-to-end low voltage cabling solutions including Cat5e, Cat6, Cat6a, and Fiber Optic infrastructure.</p>
      </article>
      <article class="card">
        <svg viewBox="0 0 24 24" fill="none" stroke="#d32a20" stroke-width="2"><path d="M2 9a15 15 0 0 1 20 0M5 13a10 10 0 0 1 14 0M8.5 16.5a5 5 0 0 1 7 0"/><circle cx="12" cy="20" r="1"/></svg>
        <h3>Wi-Fi Infrastructure</h3>
        <p>Enterprise-grade wireless network design, heatmap analysis, and deployment for seamless connectivity.</p>
      </article>
      <article class="card">
        <svg viewBox="0 0 24 24" fill="none" stroke="#d32a20" stroke-width="2"><path d="M3 5l14 5-2 5-14-5z"/><path d="M17 10l4-1v6l-5-1"/><path d="M6 12l-1 5H2"/></svg>
        <h3>Security Cameras</h3>
        <p>Advanced surveillance systems, access control, and physical security integrations for maximum protection.</p>
      </article>
    </div>
  </div>
</section>

<footer class="site-footer">
  <div class="wrap">
    <div class="footer-top">
      <div class="footer-brand">
        <div class="brand"><span class="brand-mark"></span>Wirenexa</div>
        <p>Wirenexa is a local group of IT professionals, dedicated to fast, reliable and honest service. No job is too big or too small, get in touch today for solutions to all your IT infrastructure needs!</p>
      </div>
      <div class="footer-col">
        <h4>QUICK LINKS</h4>
        <ul><li>About Us</li><li>Services</li><li>Contact</li></ul>
      </div>
      <div class="footer-col">
        <h4>REACH US</h4>
        <ul><li class="mono">National: (888) 555-0142</li><li class="mono">Local: 703-555-0187</li><li style="color:#aaa">sales@wirenexa.com</li></ul>
      </div>
    </div>
    <div class="footer-bottom">
      <span>© 2026 Wirenexa. All rights reserved.</span>
      <nav><span>Privacy Policy</span><span>Terms of Service</span></nav>
    </div>
  </div>
</footer>
</body>
</html>
```